Business Card for my New Brokerage

Looking to get a business card design for my new Real Estate Brokerage.
I want it with Picture, Phone Number, Email, Website, Office Address
Name and Designation. Please add logo too.

Target Market(s)

Real Estate Investors or Home Buyers

Industry/Entity Type

Real Estate

Contact Information for Business Card

Name, Email, Phone Number, website, email, office address

Colors
EB3D1F
EC4F4E
F09395
F8D3D4
FCEDEE

Requirements
Must have
• Minimalistic, Clean, Modern, Photo
Nice to have
• White and Red Colors

```html
<!DOCTYPE html>
<html lang="en">
<head>
<meta charset="utf-8">
<title>Ember Realty Inc — Business Card</title>
<link rel="stylesheet" href="https://fonts.googleapis.com/css2?family=Montserrat:wght@500;600;700&family=Figtree:wght@400;600&display=swap">
<style>
  :root {
    --brand-red: #dd0c19;
    --paper: #ffffff;
    --canvas: #ffffff;
    --card-edge: #d6d6d6;
    --photo-light: #dcc4bd;
    --photo-deep: #c49c92;
  }
  * { box-sizing: border-box; margin: 0; padding: 0; }
  html, body {
    width: 1200px; height: 1200px; overflow: hidden;
    background: var(--canvas);
  }
  .canvas { position: relative; width: 1200px; height: 1200px; }

  .card {
    position: absolute; left: 334px; width: 568px; height: 383px;
    background: var(--paper); border: 1px solid var(--card-edge);
    overflow: hidden;
  }
  .card--front { top: 178px; }
  .card--back  { top: 588px; }

  .wordmark {
    font-family: "Montserrat", sans-serif; font-weight: 700;
    color: var(--brand-red); text-align: center; line-height: 1;
  }
  .wordmark__name { display: block; letter-spacing: 0.01em; }
  .wordmark__sub  { display: block; letter-spacing: 0.28em; }

  .card--front .wordmark {
    position: absolute; left: 0; right: 0; top: 148px;
  }
  .card--front .wordmark__name { font-size: 70px; }
  .card--front .wordmark__sub  { font-size: 19px; margin-top: 10px; padding-left: 0.28em; }

  .hero-band { position: absolute; top: 41px; left: 0; width: 568px; height: 164px; }
  .hero-band__accent {
    position: absolute; left: 0; top: 0; width: 163px; height: 164px;
    background: var(--brand-red);
  }
  .hero-band__photo {
    position: absolute; left: 174px; top: 0; width: 173px; height: 164px;
    background: linear-gradient(120deg, var(--photo-light), var(--photo-deep));
  }
  .hero-band__contact {
    position: absolute; left: 359px; top: 0; width: 209px; height: 164px;
    background: var(--brand-red); color: var(--paper);
    font-family: "Figtree", sans-serif;
    padding: 58px 0 0 54px;
  }
  .agent__name {
    font-family: "Montserrat", sans-serif; font-weight: 700;
    font-size: 14.5px; line-height: 19px;
  }
  .agent__line { font-size: 14px; line-height: 19px; }

  .footer { position: absolute; top: 286px; left: 0; width: 568px; height: 60px; }
  .footer .wordmark { position: absolute; left: 44px; top: 8px; width: 136px; }
  .footer .wordmark__name { font-size: 34px; }
  .footer .wordmark__sub  { font-size: 9.5px; margin-top: 4px; padding-left: 0.28em; }

  .footer__info {
    position: absolute; top: 12px;
    font-family: "Figtree", sans-serif; color: var(--brand-red);
    font-size: 14px; line-height: 19px;
  }
  .footer__web { left: 223px; }
  .footer__web strong { font-weight: 600; }
  .footer__office { left: 374px; }
</style>
</head>
<body>
<main class="canvas">

  <section class="card card--front" aria-label="Card front">
    <div class="wordmark">
      <span class="wordmark__name">EMBER</span>
      <span class="wordmark__sub">REALTY INC</span>
    </div>
  </section>

  <section class="card card--back" aria-label="Card back">
    <div class="hero-band">
      <div class="hero-band__accent"></div>
      <div class="hero-band__photo" role="img" aria-label="Portrait photo of the agent"></div>
      <div class="hero-band__contact">
        <p class="agent__name">JOHN DOE</p>
        <p class="agent__line">john@emberrealty.com</p>
        <p class="agent__line">123 456 789</p>
      </div>
    </div>

    <div class="footer">
      <div class="wordmark">
        <span class="wordmark__name">EMBER</span>
        <span class="wordmark__sub">REALTY INC</span>
      </div>
      <p class="footer__info footer__web"><strong>www.emberrealty.com</strong><br>info@emberrealty.com</p>
      <p class="footer__info footer__office">Street xxxx, 123<br>456 xxx xxxxxx</p>
    </div>
  </section>

</main>
</body>
</html>
```